Investment Business - Biz Card Design

Using the attached logo files, please create a superior business card design for Tarnwell Holdings.

The "back" of the card should feature the logo (either in colour, or white/black over a feature colour)

The "front" of the card should feature: name, email, and phone

The design should be minimal and clean.

Target Market(s)

Business owners who need our investment services.

Industry/Entity Type

Business

```html
<!DOCTYPE html>
<html lang="en">
<head>
<meta charset="utf-8">
<title>Tarnwell Holdings — Business Card</title>
<link href="https://fonts.googleapis.com/css2?family=Montserrat:wght@400;600;700&family=Lato:wght@400&display=swap" rel="stylesheet">
<style>
  :root {
    --backdrop: #e9ebee;
    --card-ink: #0b0d19;
    --edge-cyan: #6fd3e0;
    --brand-blue: #3e4fb3;
    --name-white: #f2f4f8;
    --detail-grey: #8a93a8;
    --rule-cyan: #3fb7c9;
  }
  * { box-sizing: border-box; margin: 0; padding: 0; }
  html, body {
    width: 1200px;
    height: 800px;
    overflow: hidden;
    background: var(--backdrop);
  }
  .sheet {
    width: 1200px;
    height: 800px;
    display: flex;
    align-items: center;
    justify-content: center;
    gap: 60px;
  }
  .card {
    position: relative;
    width: 525px;
    height: 300px;
    background: var(--card-ink);
    border: 3px solid var(--edge-cyan);
    border-radius: 4px;
    box-shadow: 0 10px 30px rgba(20, 30, 50, 0.18);
  }

  /* Back: centred wordmark */
  .card-back {
    display: flex;
    align-items: center;
    justify-content: center;
  }
  .brand-mark {
    display: flex;
    align-items: center;
    gap: 12px;
  }
  .brand-square {
    width: 14px;
    height: 14px;
    background: var(--brand-blue);
    flex: none;
  }
  .brand-name {
    font-family: "Montserrat", sans-serif;
    font-weight: 600;
    font-size: 26px;
    letter-spacing: 0.14em;
    text-transform: uppercase;
    color: var(--brand-blue);
    white-space: nowrap;
  }

  /* Front: contact details */
  .card-front {
    padding: 34px 34px 0 34px;
  }
  .holder-name {
    font-family: "Montserrat", sans-serif;
    font-weight: 700;
    font-size: 17px;
    letter-spacing: 0.12em;
    text-transform: uppercase;
    color: var(--name-white);
  }
  .name-rule {
    margin-top: 12px;
    height: 1px;
    background: var(--rule-cyan);
    width: 100%;
  }
  .contact-line {
    margin-top: 12px;
    font-family: "Lato", sans-serif;
    font-size: 10.5px;
    letter-spacing: 0.04em;
    color: var(--detail-grey);
    display: flex;
    gap: 8px;
    white-space: nowrap;
  }
  .contact-sep { color: var(--rule-cyan); }
  .front-brand {
    position: absolute;
    right: 34px;
    bottom: 44px;
    display: flex;
    align-items: center;
    gap: 8px;
  }
  .front-brand .brand-square { width: 8px; height: 8px; }
  .front-brand .brand-name { font-size: 13px; }
  .base-rule {
    position: absolute;
    left: 34px;
    right: 34px;
    bottom: 34px;
    height: 1px;
    background: var(--rule-cyan);
  }
</style>
</head>
<body>
  <main class="sheet">
    <section class="card card-back" aria-label="Card back">
      <div class="brand-mark">
        <span class="brand-square"></span>
        <span class="brand-name">Tarnwell Holdings</span>
      </div>
    </section>

    <section class="card card-front" aria-label="Card front">
      <h1 class="holder-name">Jonah Reed</h1>
      <div class="name-rule"></div>
      <p class="contact-line">
        <span>jonahreed@tarnwellholdings.com</span>
        <span class="contact-sep">|</span>
        <span>tarnwellholdings.com</span>
        <span class="contact-sep">|</span>
        <span>000 · 2468 · 1357</span>
      </p>
      <div class="front-brand">
        <span class="brand-square"></span>
        <span class="brand-name">Tarnwell Holdings</span>
      </div>
      <div class="base-rule"></div>
    </section>
  </main>
</body>
</html>
```